Political themed graphic for contemporary church sermon series

Contemporary church in California need a graphic design for a sermon series. The sermon series will be focused on the upcoming presidential election. The sermon series is titled for the question "who will be the next president":

Title: 45
Subtitle: Who will it be / Does it matter

The design should use red, white and blue and should possibly have the cedar hall in the graphic somewhere. Maybe like a watermark or something to that effect.

Target Market(s)

Contemporary design,

Industry/Entity Type

Church

Font styles to use
Serif
Sans Serif

Colors
0555a3
ec1f27
ffffff

Requirements
Must have
• Political theme, red, white and blue (contemporary color palette). Cedar hall screened back in the design somewhere.
• the title large: 45
• and subtitle: Who will it be | Does it matter
Should not have
• I'm not looking for cheesy graphics with elephant and a donkey.

```html
<!DOCTYPE html>
<html lang="en">
<head>
<meta charset="utf-8">
<title>45 — Sermon Series</title>
<link rel="stylesheet" href="https://fonts.googleapis.com/css2?family=Bitter:wght@800&family=Source+Sans+3:wght@600;700;800&display=swap">
<style>
  :root {
    --blue: #0555a3;
    --blue-band: #2a5fb0;
    --blue-deep: #1d4c9c;
    --red: #ec1f27;
    --red-deep: #c5171e;
    --red-dark: #7c1014;
    --white: #ffffff;
    --grey: #c9c9c9;
    --stage: #111111;
  }
  html, body {
    margin: 0;
    width: 1200px;
    height: 1200px;
    overflow: hidden;
    background: var(--stage);
  }
  .poster {
    position: absolute;
    left: 245px;
    top: 0;
    width: 710px;
    height: 1200px;
    display: block;
  }
  .poster-bg { fill: var(--white); }
  .band-blue { fill: var(--blue-band); }
  .star { fill: var(--white); }
  .badge-disc { fill: var(--red); }
  .badge-number {
    font-family: "Source Sans 3", sans-serif;
    font-weight: 800;
    font-style: italic;
    font-size: 76px;
    fill: var(--white);
    stroke: var(--red-deep);
    stroke-width: 2;
  }
  .headline {
    font-family: "Bitter", serif;
    font-weight: 800;
    font-size: 41px;
  }
  .headline-blue { fill: var(--blue); }
  .headline-red { fill: var(--red-deep); }
  .year {
    font-family: "Source Sans 3", sans-serif;
    font-weight: 700;
    font-size: 52px;
    fill: var(--blue);
    letter-spacing: -1px;
  }
  .parties {
    font-family: "Source Sans 3", sans-serif;
    font-weight: 700;
    font-size: 7px;
    fill: var(--blue);
  }
  .election-top {
    font-family: "Source Sans 3", sans-serif;
    font-weight: 700;
    font-size: 17px;
    fill: var(--red-deep);
  }
  .election-main {
    font-family: "Source Sans 3", sans-serif;
    font-weight: 700;
    font-size: 23px;
    fill: var(--red-deep);
  }
  .hall-mark { fill: var(--grey); }
</style>
</head>
<body>
<svg class="poster" viewBox="0 0 509 860" xmlns="http://www.w3.org/2000/svg">
  <defs>
    <linearGradient id="redBand" x1="0" y1="0" x2="0.3" y2="1">
      <stop offset="0" stop-color="var(--red-dark)"/>
      <stop offset="0.35" stop-color="var(--red-deep)"/>
      <stop offset="0.7" stop-color="var(--red)"/>
      <stop offset="1" stop-color="var(--red-deep)"/>
    </linearGradient>
    <linearGradient id="bluePortrait" x1="0" y1="0" x2="0" y2="1">
      <stop offset="0" stop-color="var(--blue-band)" stop-opacity="0"/>
      <stop offset="0.4" stop-color="#3b78c8"/>
      <stop offset="0.7" stop-color="var(--blue-deep)"/>
      <stop offset="1" stop-color="var(--blue-band)" stop-opacity="0"/>
    </linearGradient>
    <path id="star" d="M0,-18 4.2,-5.8 17.1,-5.6 6.8,2.2 10.6,14.6 0,7.2 -10.6,14.6 -6.8,2.2 -17.1,-5.6 -4.2,-5.8Z"/>
  </defs>

  <rect class="poster-bg" width="509" height="860"/>

  <!-- blue band -->
  <path class="band-blue" d="M350,0 L509,0 L509,860 L265,860 C300,800 340,700 350,600 C358,500 378,350 370,250 C362,150 350,80 350,0 Z"/>
  <path role="img" aria-label="Blue-toned portrait photograph of a candidate" fill="url(#bluePortrait)"
        d="M355,250 C365,300 360,400 352,450 C348,520 350,560 350,600 L509,600 L509,250 Z"/>

  <!-- red band with portrait -->
  <path role="img" aria-label="Red-toned portrait photograph of a candidate" fill="url(#redBand)"
        d="M80,0 L250,0 C292,120 302,300 320,500 C330,650 335,780 350,860 L320,860 C318,760 300,620 250,520 C200,420 150,330 120,250 C95,190 45,150 0,135 L0,65 C40,60 70,40 80,0 Z"/>

  <!-- stars -->
  <use href="#star" class="star" x="440" y="172"/>
  <use href="#star" class="star" x="474" y="237"/>
  <use href="#star" class="star" x="404" y="280"/>
  <use href="#star" class="star" x="454" y="338"/>
  <use href="#star" class="star" x="440" y="628"/>
  <use href="#star" class="star" x="378" y="665"/>
  <use href="#star" class="star" x="398" y="735"/>

  <!-- title badge -->
  <circle class="badge-disc" cx="384" cy="87" r="60"/>
  <text class="badge-number" x="393" y="113" text-anchor="middle">45</text>

  <!-- subtitle -->
  <text class="headline headline-blue" x="43" y="538">WHO WILL</text>
  <text class="headline headline-blue" x="43" y="582">IT BE</text>
  <text class="headline headline-red" x="43" y="660">DOES IT</text>
  <text class="headline headline-red" x="43" y="704">MATTER</text>

  <!-- footer -->
  <text class="year" x="46" y="830">2016</text>
  <text class="parties" x="47" y="842">DEMOCRATS VS REPUBLICANS</text>
  <rect class="hall-mark" role="img" aria-label="Cedar hall building illustration" x="178" y="785" width="152" height="58"/>
  <text class="election-top" x="372" y="808">PRESIDENTIAL</text>
  <text class="election-main" x="372" y="835">ELECTION</text>
</svg>
</body>
</html>
```